ESCORT DIRECTORY

This website is an advertising and information resource , we only sell advertisement space.
The requirement:
-- 7 Banners with different size
--sexy girl on the banner
-- the sexy girl will have different position on each banner
--I want my logo on the banner (Upload files)
-- I want the word : " ADVERTISE FOR FREE" in a beautiful presentation

```html
<!DOCTYPE html>
<html lang="en">
<head>
<meta charset="utf-8">
<title>Escort Directory – Advertise for Free</title>
<link rel="stylesheet" href="https://fonts.googleapis.com/css2?family=Bebas+Neue&family=Montserrat:wght@600;900&family=Oswald:wght@300&display=swap">
<style>
  :root {
    --backdrop: #6b6b6b;
    --card: #ffffff;
    --ink: #111111;
    --hot-pink: #ff1478;
    --soft-pink: #ff6fd8;
    --pale-pink: #ffd3f2;
    --photo-deep: #0d1e2c;
    --photo-teal: #2a5a6e;
    --photo-glow: #c2306f;
  }
  * { box-sizing: border-box; margin: 0; padding: 0; }
  html, body {
    width: 1200px;
    height: 1191px;
    overflow: hidden;
    background: var(--backdrop);
  }
  .banner {
    position: absolute;
    left: 107px;
    top: 102px;
    width: 987px;
    height: 987px;
    background: var(--card);
    box-shadow: 14px 16px 22px rgba(0, 0, 0, 0.45);
  }
  .banner > * { position: absolute; }

  .accent-top {
    left: 386px; top: 0; width: 119px; height: 329px;
    background: linear-gradient(180deg, var(--hot-pink), var(--soft-pink));
  }
  .photo-frame {
    left: 482px; top: 71px; width: 429px; height: 688px;
    border: 2px solid var(--ink);
  }
  .photo {
    left: 451px; top: 111px; width: 489px; height: 612px;
    background:
      radial-gradient(ellipse at 35% 55%, var(--photo-glow) 0%, transparent 45%),
      linear-gradient(160deg, var(--photo-teal), var(--photo-deep) 70%);
  }
  .accent-bottom {
    left: 591px; top: 686px; width: 396px; height: 131px;
    background: linear-gradient(90deg, var(--soft-pink), var(--hot-pink));
  }
  .dot-field {
    left: 718px; top: 830px; width: 247px; height: 136px;
    background: var(--pale-pink);
  }

  .brand {
    left: 25px; top: 222px;
    font-family: "Oswald", sans-serif;
    font-weight: 300;
    font-size: 60px;
    line-height: 1;
    letter-spacing: 5px;
    color: var(--ink);
  }

  .offer-tab {
    left: 0; top: 449px; width: 68px; height: 65px;
    background: linear-gradient(90deg, var(--soft-pink), var(--hot-pink));
  }
  .offer {
    left: 49px; top: 383px; width: 335px; height: 192px;
    border: 2px solid var(--ink);
    display: flex; flex-direction: column; align-items: center; justify-content: center;
    font-family: "Montserrat", sans-serif;
    color: var(--ink);
  }
  .offer-lead {
    font-weight: 600;
    font-size: 22px;
    letter-spacing: 8px;
    margin-right: -8px;
  }
  .offer-main {
    font-weight: 900;
    font-size: 98px;
    line-height: 1;
    margin-top: 2px;
  }

  .headline {
    left: 25px;
    font-family: "Bebas Neue", sans-serif;
    font-size: 158px;
    font-weight: 400;
    line-height: 1;
    letter-spacing: 5px;
    white-space: nowrap;
  }
  .headline-top {
    top: 671px;
    background: linear-gradient(180deg, var(--hot-pink), var(--soft-pink));
    -webkit-background-clip: text;
    background-clip: text;
    color: transparent;
  }
  .headline-bottom {
    top: 804px;
    color: var(--ink);
  }
</style>
</head>
<body>
  <main class="banner">
    <div class="accent-top"></div>
    <div class="photo-frame"></div>
    <div class="photo" role="img" aria-label="Photo of a model in a wet white top under falling rain, lit in pink and teal"></div>
    <div class="accent-bottom"></div>
    <div class="dot-field" role="img" aria-label="Grid of small pink dots"></div>

    <div class="brand">VELVETLIST</div>

    <div class="offer-tab"></div>
    <div class="offer">
      <span class="offer-lead">ADVERTISE FOR</span>
      <span class="offer-main">FREE</span>
    </div>

    <h1 class="headline headline-top">ESCORT</h1>
    <h2 class="headline headline-bottom">DIRECTORY</h2>
  </main>
</body>
</html>
```